Clinical Research Consulting Company needs a web design

My consulting company provides service on clinical trial design and clincal research, product safety and claim development strategy, and lecture service.

Need template and graphic design for the website of my consulting company. Website will have many different tabs (e.g., Home, About Us, Service, and Contact Us).

Like to have modern look and easy on eyes (not too many colors).

We don't perform laboratory work so please do not use pictures with people working in the laboratory. Also, the logo is added. Thanks.

Target Market(s)

Pharmaceutical and Biotech companies, dietary supplement companies, food industry

Industry/Entity Type

It Company

Number of Pages Required

4 page

Font styles to use
Sans Serif

Requirements
Must have
• hyperlink to Contact Us page
Nice to have
• pictures

```html
<!DOCTYPE html>
<html lang="en">
<head>
<meta charset="utf-8">
<title>Kelora Consulting Inc</title>
<link href="https://fonts.googleapis.com/css2?family=Questrial&family=Mulish:wght@400;600;700&family=Arimo:wght@400;700&display=swap" rel="stylesheet">
<style>
:root{
  --blue:#2a9bd0;
  --blue-dark:#2284b5;
  --blue-deep:#1f78a6;
  --blue-light:#4db8e8;
  --ink:#333;
  --grey:#777;
  --pale:#eef3f6;
  --white:#fff;
}
*{box-sizing:border-box;margin:0;padding:0}
html,body{width:1200px;height:2229px;overflow:hidden;background:var(--white)}
body{position:relative;font-family:"Arimo",Arial,sans-serif;color:var(--ink)}
.abs{position:absolute}
a{color:inherit;text-decoration:none}

/* top bar */
.topbar{left:0;top:0;width:1200px;height:45px;background:var(--blue)}
.topbar .icon-box{top:0;width:37px;height:45px;background:var(--blue-dark);display:flex;align-items:center;justify-content:center}
.topbar .contact-text{top:0;line-height:45px;font-size:11px;color:var(--white)}
.social-top{left:881px;top:0;display:flex}
.social-top span{width:37px;height:45px;border-left:1px solid rgba(255,255,255,.25);display:flex;align-items:center;justify-content:center}
.social-top span:last-child{border-right:1px solid rgba(255,255,255,.25)}
.social-top i{width:9px;height:9px;border-radius:50%;background:var(--white);display:block}

/* header */
.header{left:0;top:45px;width:1200px;height:135px;background:var(--white);box-shadow:0 2px 4px rgba(0,0,0,.08);z-index:2}
.brand{left:180px;top:52px;display:flex;align-items:center;gap:10px;font-family:"Questrial",sans-serif;font-size:26px;color:#3a3a3a}
.brand .mark{width:18px;height:18px;background:var(--blue)}
.nav{left:613px;top:53px;display:flex;gap:0;font-family:"Questrial",sans-serif;font-size:16px}
.nav a{display:block;height:30px;line-height:30px;padding:0 12px;margin-right:16px;color:#222}
.nav a.active{background:var(--blue);color:var(--white)}

/* hero */
.hero{left:0;top:180px;width:1200px;height:504px;background:linear-gradient(90deg,#e8eef2 0%,#f3f6f8 40%,#dfe7ee 70%,#5f8fbf 100%)}
.hero-title{left:182px;top:286px;font-family:"Mulish",sans-serif;font-weight:700;font-size:37px;line-height:46px;color:#2f3a44}
.hero-title .accent{color:var(--blue-light);display:block}
.hero-badge{left:173px;top:425px;width:433px;height:105px;background:rgba(42,155,208,.9);display:flex;align-items:center;padding-left:30px;gap:22px}
.hero-badge p{font-family:"Questrial",sans-serif;font-size:13px;line-height:18px;color:var(--white);text-transform:uppercase}
.hero-badge b{font-weight:700}
.slider-arrow{top:402px;width:50px;height:50px;border:2px solid rgba(255,255,255,.7);border-radius:50%;display:flex;align-items:center;justify-content:center}
.dots{left:578px;top:644px;display:flex;gap:8px}
.dots i{width:9px;height:9px;border-radius:50%;background:rgba(255,255,255,.8);display:block}
.dots i:first-child{background:var(--blue)}

/* signup */
.signup{left:0;top:684px;width:1200px;height:134px;background:var(--blue)}
.signup .lead{left:171px;top:45px;font-size:12px;color:var(--white)}
.signup h2{left:171px;top:66px;font-family:"Questrial",sans-serif;font-weight:400;font-size:23px;color:var(--white)}
.signup h2 b{font-family:"Mulish",sans-serif;font-weight:700}
.email-field{left:699px;top:41px;width:328px;height:52px;background:var(--blue-dark);display:flex}
.email-field span{flex:1;line-height:52px;padding-left:26px;font-size:11px;color:#d6ecf7}
.email-field i{width:52px;height:52px;border-left:2px solid var(--blue);display:flex;align-items:center;justify-content:center}

/* sectors */
.sector{top:860px;width:205px}
.sector .photo{width:205px;height:186px}
.sector .label{margin-top:14px;display:flex;justify-content:space-between;font-family:"Questrial",sans-serif;font-size:14px;line-height:16px;color:#444;text-transform:uppercase;padding-left:2px}

/* recruit band */
.band{left:0;top:1172px;width:1200px;height:487px;background:linear-gradient(90deg,#c9d6de 0%,#e6eef2 30%,#f1f5f7 55%,#dfe8ee 100%)}
.join{left:430px;top:1270px;width:185px;text-align:center}
.join .rule{height:1px;background:#c9d3d8;margin:0 auto}
.join h3{font-family:"Questrial",sans-serif;font-weight:400;font-size:25px;color:#333;padding:10px 0}
.join .hiring{font-family:"Arimo",sans-serif;font-weight:700;font-size:22px;color:#333;margin-top:18px}
.join .btn{display:block;width:132px;height:47px;line-height:47px;margin:22px auto 0;background:var(--blue);color:var(--white);font-weight:700;font-size:14px}
.join .sub{margin-top:18px;font-size:14px;color:#666}

.panel{left:674px;top:1222px;width:353px;height:389px;background:var(--blue);border-radius:4px;overflow:hidden;box-shadow:0 2px 6px rgba(0,0,0,.15)}
.panel .top{height:149px;background:var(--blue-deep);position:relative}
.panel h4{font-family:"Questrial",sans-serif;font-weight:400;font-size:21px;color:var(--white);text-align:center}
.field{position:absolute;height:36px;font-size:11px;color:#8a9aa3;background:#eef4f8;display:flex;align-items:center;justify-content:space-between;padding:0 12px;border-radius:2px}
.panel .search-field{background:#bfe0f0;color:#4f6f80}
.tab{position:absolute;left:150px;top:149px;width:52px;height:26px;background:var(--blue-deep);border-radius:0 0 26px 26px;display:flex;align-items:center;justify-content:center}
.advance{position:absolute;left:36px;top:344px;font-size:11px;color:var(--white);display:flex;gap:8px;align-items:center}
.go{position:absolute;left:286px;top:333px;width:36px;height:35px;background:var(--blue-deep);display:flex;align-items:center;justify-content:center;border-radius:2px}

/* social */
.social h2{position:absolute;left:0;top:1686px;width:1200px;text-align:center;font-family:"Questrial",sans-serif;font-weight:400;font-size:30px;color:var(--blue)}
.social .rule{position:absolute;left:446px;width:304px;height:1px;background:#e2e2e2}
.social .kit{position:absolute;left:0;top:1750px;width:1200px;text-align:center;font-size:11px;color:#333;letter-spacing:.5px}
.social-icons{left:484px;top:1822px;display:flex;gap:43px}
.social-icons i{width:24px;height:24px;border-radius:50%;background:#b8b8b8;display:block}

/* footer */
.footer{left:0;top:1880px;width:1200px;height:349px;background:var(--blue)}
.footer .badge{left:518px;top:11px;width:156px;height:156px;border-radius:50%;background:var(--white);display:flex;align-items:center;justify-content:center;font-family:"Questrial",sans-serif;font-size:26px;color:var(--blue)}
.footer .line{left:394px;top:164px;width:412px;height:1px;background:rgba(255,255,255,.45)}
.footer-nav{left:0;top:176px;width:1200px;text-align:center;font-size:14px;color:var(--white)}
.footer-nav span{margin:0 14px}
.copyright{left:0;top:236px;width:1200px;text-align:center;font-size:14px;color:var(--white)}
.privacy{left:0;top:271px;width:1200px;text-align:center;font-size:12px;color:#a9d7ee}
</style>
</head>
<body>

<div class="abs topbar">
  <div class="abs icon-box" style="left:173px">
    <svg width="14" height="14" viewBox="0 0 24 24"><path d="M6.6 10.8a15 15 0 0 0 6.6 6.6l2.2-2.2a1 1 0 0 1 1-.25 11 11 0 0 0 3.6.6 1 1 0 0 1 1 1V20a1 1 0 0 1-1 1A17 17 0 0 1 3 4a1 1 0 0 1 1-1h3.5a1 1 0 0 1 1 1 11 11 0 0 0 .6 3.6 1 1 0 0 1-.25 1z" fill="#fff"/></svg>
  </div>
  <div class="abs contact-text" style="left:219px">(41) 41-555-0184</div>
  <div class="abs icon-box" style="left:325px">
    <svg width="16" height="14" viewBox="0 0 24 20"><path d="M1 9 23 1 17 19 11 13 19 5 9 11z" fill="none" stroke="#fff" stroke-width="2" stroke-linejoin="round"/></svg>
  </div>
  <div class="abs contact-text" style="left:368px">info@keloraconsulting.com</div>
  <div class="abs social-top"><span><i></i></span><span><i></i></span><span><i></i></span><span><i></i></span></div>
</div>

<header class="abs header">
  <div class="abs brand"><span class="mark"></span>Kelora Consulting Inc</div>
  <nav class="abs nav">
    <a class="active" href="#">Home</a><a href="#">About</a><a href="#">Services</a><a href="#">Blog</a><a href="#contact">Contact</a>
  </nav>
</header>

<section class="abs hero" role="img" aria-label="Photo of a senior researcher in a white coat in a bright office">
</section>
<h1 class="abs hero-title">Leading global consulting firm<span class="accent">focused exclusively on life sciences</span></h1>
<div class="abs hero-badge">
  <svg width="40" height="44" viewBox="0 0 40 44"><path d="M6 2v12a10 10 0 0 0 20 0V2M20 24v8a8 8 0 0 0 16 0v-6" fill="none" stroke="#fff" stroke-width="2.5" stroke-linecap="round"/><circle cx="36" cy="22" r="3.5" fill="none" stroke="#fff" stroke-width="2.5"/></svg>
  <p>Guided clinically by the top international<br>thought <b>leaders !</b></p>
</div>
<div class="abs slider-arrow" style="left:59px"><svg width="12" height="18" viewBox="0 0 12 18"><path d="M10 2 3 9l7 7" fill="none" stroke="#fff" stroke-width="2"/></svg></div>
<div class="abs slider-arrow" style="left:1090px"><svg width="12" height="18" viewBox="0 0 12 18"><path d="m2 2 7 7-7 7" fill="none" stroke="#fff" stroke-width="2"/></svg></div>
<div class="abs dots"><i></i><i></i><i></i></div>

<section class="abs signup">
  <p class="abs lead">Be The First To Receive Clincal Research, product safety and claim development strategy</p>
  <h2 class="abs"><b>SIGN UP</b> FOR OUR LECTURE SERVICES</h2>
  <div class="abs email-field"><span>Enter Your Email Address</span><i><svg width="20" height="18" viewBox="0 0 24 20"><path d="M1 9 23 1 17 19 11 13 19 5 9 11z" fill="none" stroke="#fff" stroke-width="2" stroke-linejoin="round"/></svg></i></div>
</section>

<div class="abs sector" style="left:167px">
  <div class="photo" role="img" aria-label="Photo of pharmaceutical vials" style="background:linear-gradient(160deg,#0f5fa8,#3fa6e6 60%,#bfe4f7)"></div>
  <div class="label"><span>Pharmaceutical<br>Companies</span><svg width="8" height="14" viewBox="0 0 8 14"><path d="m1 2 5 5-5 5" fill="none" stroke="#2a9bd0" stroke-width="2"/></svg></div>
</div>
<div class="abs sector" style="left:385px">
  <div class="photo" role="img" aria-label="Photo of a seedling in a petri dish" style="background:linear-gradient(160deg,#9cc8e4,#4d84b8 55%,#c3d9ea)"></div>
  <div class="label"><span>Biotech<br>Companies</span><svg width="8" height="14" viewBox="0 0 8 14"><path d="m1 2 5 5-5 5" fill="none" stroke="#2a9bd0" stroke-width="2"/></svg></div>
</div>
<div class="abs sector" style="left:600px">
  <div class="photo" role="img" aria-label="Photo of supplement bottles on store shelves" style="background:linear-gradient(160deg,#6e4a2c,#b98a55 50%,#e2c9a0)"></div>
  <div class="label"><span>Dietary Supplement<br>Companies</span><svg width="8" height="14" viewBox="0 0 8 14"><path d="m1 2 5 5-5 5" fill="none" stroke="#2a9bd0" stroke-width="2"/></svg></div>
</div>
<div class="abs sector" style="left:818px">
  <div class="photo" role="img" aria-label="Photo of a food production line" style="background:linear-gradient(170deg,#3b4a55,#8a97a0 45%,#d29b4a)"></div>
  <div class="label"><span>Food Industry</span><svg width="8" height="14" viewBox="0 0 8 14"><path d="m1 2 5 5-5 5" fill="none" stroke="#2a9bd0" stroke-width="2"/></svg></div>
</div>

<section class="abs band" role="img" aria-label="Photo of a researcher working in a bright lab"></section>
<div class="abs join">
  <svg width="36" height="50" viewBox="0 0 36 50"><path d="M18 2v28M8 20l10 10 10-10" fill="none" stroke="#2a9bd0" stroke-width="5"/><rect x="2" y="42" width="32" height="5" fill="#2a9bd0"/></svg>
  <div class="rule" style="width:185px;margin-top:14px"></div>
  <h3>JOIN OUR TEAM</h3>
  <div class="rule" style="width:185px"></div>
  <p class="hiring">We're Hiring!</p>
  <a class="btn" href="#">Click Here</a>
  <p class="sub">to View Open Positions !</p>
</div>

<div class="abs panel">
  <div class="top">
    <h4 style="padding-top:28px">SEARCH PUBLISHED REPORTS !</h4>
    <div class="field search-field" style="left:36px;top:75px;width:286px">Enter Search Items
      <svg width="12" height="12" viewBox="0 0 12 12"><circle cx="5" cy="5" r="3.8" fill="none" stroke="#2a7fb0" stroke-width="1.5"/><path d="m8 8 3 3" stroke="#2a7fb0" stroke-width="1.5"/></svg></div>
  </div>
  <div class="tab"><svg width="14" height="9" viewBox="0 0 14 9"><path d="m2 2 5 5 5-5" fill="none" stroke="#fff" stroke-width="2"/></svg></div>
  <h4 style="margin-top:38px">CONSULT AN EXPERT</h4>
  <div class="field" style="left:36px;top:233px;width:286px">Select Industry<svg width="10" height="6" viewBox="0 0 10 6"><path d="m1 1 4 4 4-4" fill="none" stroke="#aaa"/></svg></div>
  <div class="field" style="left:36px;top:275px;width:139px">choose type<svg width="10" height="6" viewBox="0 0 10 6"><path d="m1 1 4 4 4-4" fill="none" stroke="#aaa"/></svg></div>
  <div class="field" style="left:183px;top:275px;width:139px">choose type<svg width="10" height="6" viewBox="0 0 10 6"><path d="m1 1 4 4 4-4" fill="none" stroke="#aaa"/></svg></div>
  <div class="advance">Advance Settings <svg width="10" height="6" viewBox="0 0 10 6"><path d="m1 1 4 4 4-4" fill="none" stroke="#fff"/></svg></div>
  <div class="go"><svg width="14" height="14" viewBox="0 0 12 12"><circle cx="5" cy="5" r="3.8" fill="none" stroke="#fff" stroke-width="1.5"/><path d="m8 8 3 3" stroke="#fff" stroke-width="1.5"/></svg></div>
</div>

<section class="social">
  <h2>SOCIAL NETWORKING !</h2>
  <div class="rule" style="top:1739px"></div>
  <p class="kit">KEEP IN TOUCH</p>
  <div class="rule" style="top:1776px"></div>
  <div class="abs social-icons"><i></i><i></i><i></i><i></i></div>
</section>

<footer class="abs footer" id="contact">
  <div class="abs badge">Kelora</div>
  <div class="abs line"></div>
  <nav class="abs footer-nav"><a href="#">Home</a><span>/</span><a href="#">About</a><span>/</span><a href="#">Services</a><span>/</span><a href="#">Blog</a><span>/</span><a href="#contact">Contact</a></nav>
  <p class="abs copyright">Copyrights © kelora consulting inc. All Rights Reserved.</p>
  <p class="abs privacy">Privacy Policy</p>
</footer>

</body>
</html>
```